Tidewell HVAC WordPress website design

Design a new modern, clean, website for HVAC mechanical business that uses company logo/colors for branding and recognition. Files attached are just for band and color information. Here is a website design that appeals to me https://www.quillerbyhomes.example/

A clear description of who we are and what we do

An easily-navigated site map

An easily-navigated site map for mobile devices

Easy-to-find contact information

Obvious call to action for service, installs or to schedule estimates

about us page

Provide a way for potential customers to contact us via text or email

provide a way that allows a customer to upload a picture to request a service call or quote.
Updates

I'm looking for the design to be completed in WordPress

Industry/Entity Type

HVAC Mechanical & Building Automation / Controls contractor

Coding

Coded - Design and coding required

Number of Pages Required

5+ page

Colors
0054AA
0677BA
7BADD7
CADEEF
E8F1F8

Requirements
Must have
• Design a new modern, clean, website for HVAC mechanical business that uses company logo/colors for branding and recognition. Files attached are just for band and color information. Here is a website design that appeals to me https://www.quillerbyhomes.example/ A clear description of who we are and what we do An easily-navigated site map An easily-navigated site map for mobile devices Easy-to-find contact information Obvious call to action for service, installs or to schedule estimates about us page Provide a way for potential customers to contact us via text or email provide a way that allows a customer to upload a picture to request a service call or quote.
Nice to have

```html
<!DOCTYPE html>
<html lang="en">
<head>
<meta charset="utf-8">
<title>Tidewell HVAC — Installation, Maintenance, Servicing & Repairs</title>
<link rel="stylesheet" href="https://fonts.googleapis.com/css2?family=Inter:wght@400;500;600;700&display=swap">
<style>
:root{
  --navy:#0d3a8c;
  --blue:#0054AA;
  --bright:#0677BA;
  --btn:#0a74d0;
  --sky:#7BADD7;
  --pale:#CADEEF;
  --mist:#E8F1F8;
  --ink:#1b2a45;
  --text:#2e3440;
  --muted:#6b7484;
  --black:#0b0b0d;
  --white:#ffffff;
}
*{box-sizing:border-box;margin:0;padding:0}
html,body{width:1200px;height:4643px;overflow:hidden}
body{font-family:"Inter",Arial,sans-serif;color:var(--text);background:var(--white)}
.page{width:1200px;height:4643px;position:relative;overflow:hidden}
.btn{display:inline-block;background:var(--btn);color:var(--white);font-size:12px;font-weight:600;letter-spacing:.3px;text-transform:uppercase;padding:13px 20px;border:none}
.eyebrow{display:flex;align-items:center;gap:12px;font-size:11px;font-weight:600;color:var(--blue);text-transform:uppercase;letter-spacing:.5px}
.eyebrow::before{content:"";width:72px;height:2px;background:var(--blue)}
.eyebrow.center::after{content:"";width:58px;height:1px;background:currentColor}
.eyebrow.center::before{width:58px;height:1px;background:currentColor}

/* top bar */
.topbar{height:37px;background:var(--black);display:flex;justify-content:flex-end;align-items:center;padding-right:105px;gap:18px}
.topbar .phone{color:var(--white);font-size:13px;font-weight:500;display:flex;align-items:center;gap:7px}
.topbar .btn{padding:10px 12px;font-size:11px}

/* nav */
.nav{height:78px;background:linear-gradient(90deg,var(--blue),var(--bright));display:flex;align-items:center;justify-content:space-between;padding:0 100px 0 72px}
.brand{display:flex;align-items:center;gap:10px;color:var(--white);font-size:26px;font-weight:700}
.brand .dot{width:22px;height:22px;border-radius:50%;background:var(--white)}
.menu{display:flex;gap:34px;list-style:none;color:var(--white);font-size:14px;font-weight:500}

/* hero */
.hero{height:600px;position:relative;overflow:hidden}
.hero-bg{position:absolute;inset:0;background:linear-gradient(90deg,#123f95 0%,#2353a6 35%,#6e86b4 62%,#9aa9c3 100%)}
.hero-content{position:absolute;left:90px;top:90px;color:var(--white)}
.hero-content .kicker{font-size:17px;margin-bottom:28px}
.hero-content h1{font-size:40px;font-weight:500;line-height:1.26;margin-bottom:52px}
.hero-content .btn{padding:16px 10px}
.van{position:absolute;right:16px;bottom:20px;width:520px;height:260px;border-radius:60px 90px 30px 30px;background:linear-gradient(160deg,#f4f6fa 0%,#d8dde6 55%,#3f68b0 100%)}

/* about */
.about{height:810px;position:relative}
.about-photo-frame{position:absolute;left:90px;top:200px;width:340px;height:410px;background:linear-gradient(180deg,var(--blue),#1f68c8)}
.about-photo{position:absolute;left:114px;top:224px;width:318px;height:370px;background:linear-gradient(160deg,#a88f6a,#4f5d78 60%,#2e3f63)}
.about-text{position:absolute;left:643px;top:110px;width:400px}
.about-text h2{font-size:23px;font-weight:600;color:var(--ink);line-height:1.3;margin:14px 0 22px}
.about-text p{font-size:11.5px;line-height:1.75;color:var(--text)}
.feature{display:flex;gap:18px;margin-top:30px}
.feature .ico{flex:0 0 52px;height:52px;border-radius:50%;border:3px solid var(--pale);background:var(--blue);display:flex;align-items:center;justify-content:center}
.feature h3{font-size:17px;font-weight:500;color:var(--blue);margin:4px 0 12px}
.feature p{font-size:11px}
.about-text .btn{margin:34px 0 0 14px;text-transform:none;font-size:12px;padding:12px 18px}

/* solutions */
.solutions{height:555px;background:linear-gradient(180deg,var(--blue) 0%,#0b5fc0 60%,#1a74d6 100%);color:var(--white);text-align:center;padding-top:66px}
.solutions .eyebrow{justify-content:center;color:var(--white)}
.solutions h2{font-size:34px;font-weight:500;margin:20px 0 34px}
.cards{display:flex;justify-content:center;gap:15px}
.card{width:207px;height:192px;background:var(--white);position:relative;text-align:left;padding:38px 28px}
.card .num{position:absolute;right:12px;top:12px;font-size:64px;font-weight:700;color:#eef1f6}
.card svg{position:relative}
.card h3{position:absolute;left:0;right:0;bottom:42px;text-align:center;color:var(--ink);font-size:16px;font-weight:600;line-height:1.2}

/* specialties */
.specialties{height:640px;text-align:center;padding-top:74px;background:linear-gradient(180deg,#fff,#f6f8fb)}
.specialties h2{font-size:35px;font-weight:600;color:var(--ink);margin-bottom:22px}
.specialties p{width:475px;margin:0 auto;font-size:11.5px;line-height:1.8;color:var(--text)}
.gallery{position:relative;display:flex;justify-content:center;gap:13px;margin:64px 0 36px}
.gallery .shot{width:165px;height:126px}
.arrow{position:absolute;top:50%;transform:translateY(-50%);width:26px;height:26px;border-radius:50%;background:var(--white);display:flex;align-items:center;justify-content:center;box-shadow:0 1px 4px rgba(0,0,0,.25)}

/* feedback */
.feedback{height:540px;background:linear-gradient(180deg,#dfe7f1 0%,#eef2f7 50%,#d9e1ec 100%);padding-top:98px;text-align:center}
.feedback h2{font-size:24px;font-weight:600;color:var(--ink);margin-bottom:40px}
.reviews{display:flex;justify-content:center;gap:13px}
.review{width:207px;height:208px;background:var(--white);text-align:left;padding:20px 16px;position:relative}
.stars{display:flex;gap:3px;margin-bottom:16px}
.review p{font-size:11px;font-weight:500;line-height:1.75;color:var(--ink)}
.reviewer{position:absolute;left:16px;right:16px;bottom:18px;border-top:1px solid #e5e8ee;padding-top:14px;display:flex;gap:10px;align-items:center}
.reviewer .av{width:26px;height:26px;border-radius:50%;background:var(--sky)}
.reviewer b{display:block;font-size:11px;font-weight:600;color:var(--ink)}
.reviewer span{font-size:8px;color:var(--muted)}

/* call to action */
.cta{height:384px;background:var(--navy);color:var(--white);text-align:center;padding-top:108px}
.cta h2{font-size:22px;font-weight:500;line-height:1.32;text-transform:uppercase}
.cta-row{display:flex;justify-content:center;align-items:center;gap:18px;margin-top:48px}
.cta-row .phone{display:flex;align-items:center;gap:12px;font-size:17px}

/* contact */
.contact{height:674px;position:relative}
.contact-info{position:absolute;left:166px;top:100px;list-style:none}
.contact-info li{display:flex;gap:12px;font-size:11.5px;line-height:1.5;margin-bottom:16px;color:var(--ink)}
.contact-info .ci{flex:0 0 20px;height:20px;border-radius:50%;background:var(--blue);display:flex;align-items:center;justify-content:center}
.map{position:absolute;left:162px;top:260px;width:372px;height:220px;background:linear-gradient(135deg,#e7ecf1,#d8e6d6 60%,#e9e4d8)}
.form{position:absolute;left:610px;top:80px;width:410px}
.form h2{font-size:26px;font-weight:500;color:var(--ink);line-height:1.25;margin-bottom:34px}
.fields{display:grid;grid-template-columns:1fr 1fr;gap:15px 14px}
.field{height:40px;background:#f2f3f5;font-size:10.5px;color:var(--ink);padding:13px 12px}
.field.wide{grid-column:1/3;height:82px}
.form .btn{margin-top:26px;width:107px;text-align:center;padding:14px 0}

/* footer */
.footer{height:286px;background:var(--black);color:var(--white);position:relative}
.footer .brand{position:absolute;left:90px;top:100px}
.fcol{position:absolute;top:60px}
.fcol h4{font-size:13px;font-weight:600;margin-bottom:20px;letter-spacing:.3px}
.fcol ul{list-style:none;font-size:11px;line-height:1.5}
.fcol li{margin-bottom:10px}
.fcol .ic{display:flex;gap:10px}
.fcol .ic i{flex:0 0 18px;height:18px;border-radius:50%;background:var(--btn);display:block}
.copy{height:39px;background:var(--blue);color:var(--white);font-size:11px;display:flex;align-items:center;justify-content:space-between;padding:0 110px 0 104px}
.socials{display:flex;gap:12px}
.socials span{width:13px;height:13px;border-radius:50%;background:var(--white)}
</style>
</head>
<body>
<div class="page">

  <div class="topbar">
    <span class="phone">
      <svg width="14" height="14" viewBox="0 0 24 24" fill="none" stroke="#fff" stroke-width="2"><path d="M22 16.9v3a2 2 0 0 1-2.2 2 19.8 19.8 0 0 1-8.6-3.1 19.5 19.5 0 0 1-6-6A19.8 19.8 0 0 1 2.1 4.2 2 2 0 0 1 4.1 2h3a2 2 0 0 1 2 1.7c.1.9.4 1.8.7 2.7a2 2 0 0 1-.5 2.1L8 9.8a16 16 0 0 0 6 6l1.3-1.3a2 2 0 0 1 2.1-.4c.9.3 1.8.6 2.7.7a2 2 0 0 1 1.7 2z"/></svg>
      555-014-2780
    </span>
    <span class="btn">Schedule an appointment</span>
  </div>

  <header class="nav">
    <div class="brand"><span class="dot"></span>Tidewell HVAC</div>
    <ul class="menu">
      <li>Home</li>
      <li>Services ⌄</li>
      <li>About Us</li>
      <li>Contact Us</li>
    </ul>
  </header>

  <section class="hero">
    <div class="hero-bg" role="img" aria-label="Rooftop HVAC units and ducting on a commercial building under a blue tint"></div>
    <div class="hero-content">
      <p class="kicker">Welcome to Tidewell HVAC</p>
      <h1>HVAC Installation,<br>Maintenance, Servicing<br>&amp; Repairs</h1>
      <span class="btn">Schedule an appointment</span>
    </div>
    <div class="van" role="img" aria-label="Company service van with blue branded livery"></div>
  </section>

  <section class="about">
    <div class="about-photo-frame"></div>
    <div class="about-photo" role="img" aria-label="Three technicians in blue work shirts"></div>
    <div class="about-text">
      <div class="eyebrow">About Us</div>
      <h2>With Us Your Plans Are In Safe<br>Hands</h2>
      <p>Lorem ipsum dolor sit amet consectetur. Hac in volutpat luctus in eu. Nisi diam purus quam tortor. Enim natoque metus lacus nunc ac congue. Id tempus pellentesque blandit nunc lectus orci lorem. At massa faucibus ac vel pulvinar interdum donec est. Ultrices congue rhoncus congue eget sem.</p>
      <div class="feature">
        <div class="ico"><svg width="24" height="24" viewBox="0 0 24 24" fill="#fff"><circle cx="12" cy="7" r="3.2"/><circle cx="5.5" cy="9" r="2.4"/><circle cx="18.5" cy="9" r="2.4"/><path d="M6 20c0-3.6 2.7-6 6-6s6 2.4 6 6z"/><path d="M1 19c0-2.6 1.8-4.3 4.5-4.3 1 0 1.6.2 2 .4C6 16.4 5 18 5 19z"/><path d="M23 19c0-2.6-1.8-4.3-4.5-4.3-1 0-1.6.2-2 .4 1.5 1.3 2.5 2.9 2.5 3.9z"/></svg></div>
        <div><h3>Experienced Employees</h3><p>Lorem ipsum dolor sit amet consectetur. Interdum cursus duis vitae eleifend nascetur cras viverra.</p></div>
      </div>
      <div class="feature">
        <div class="ico"><svg width="24" height="24" viewBox="0 0 24 24" fill="none" stroke="#fff" stroke-width="2.2"><circle cx="12" cy="10" r="6"/><path d="M9 10l2 2 4-4"/><path d="M8.5 15l-1.5 7 5-2.5 5 2.5-1.5-7"/></svg></div>
        <div><h3>Certified Company</h3><p>Lorem ipsum dolor sit amet consectetur. Interdum cursus duis vitae eleifend nascetur cras viverra.</p></div>
      </div>
      <span class="btn">Learn More</span>
    </div>
  </section>

  <section class="solutions">
    <div class="eyebrow center">Service</div>
    <h2>Our Solutions</h2>
    <div class="cards">
      <div class="card"><span class="num">01</span>
        <svg width="38" height="48" viewBox="0 0 24 30"><path d="M12 1c1 6 9 10 9 18a9 9 0 0 1-18 0c0-4 2-6 4-8 0 3 1 5 3 5-1-6 1-11 2-15z" fill="var(--blue)"/></svg>
        <h3>Gas Fitting/Piping</h3></div>
      <div class="card"><span class="num">02</span>
        <svg width="58" height="50" viewBox="0 0 30 26"><path d="M3 22l10-10M17 8l9 14" stroke="var(--blue)" stroke-width="4" stroke-linecap="round"/><circle cx="16" cy="6" r="4" fill="none" stroke="var(--blue)" stroke-width="3"/></svg>
        <h3>Service &amp; Installation</h3></div>
      <div class="card"><span class="num">03</span>
        <svg width="50" height="44" viewBox="0 0 30 26"><path d="M3 13L15 3l12 10" fill="none" stroke="var(--blue)" stroke-width="2.5"/><rect x="7" y="12" width="16" height="12" fill="var(--blue)"/><rect x="13" y="17" width="4" height="7" fill="#fff"/></svg>
        <h3>Residential &amp;<br>Commercrials</h3></div>
      <div class="card"><span class="num">04</span>
        <svg width="50" height="52" viewBox="0 0 26 28"><rect x="4" y="4" width="11" height="23" fill="var(--blue)"/><rect x="15" y="11" width="8" height="16" fill="var(--bright)"/><g fill="#fff"><rect x="6" y="7" width="2" height="2"/><rect x="11" y="7" width="2" height="2"/><rect x="6" y="12" width="2" height="2"/><rect x="11" y="12" width="2" height="2"/><rect x="6" y="17" width="2" height="2"/><rect x="11" y="17" width="2" height="2"/></g></svg>
        <h3>Building Automation<br>&amp; Controls</h3></div>
    </div>
  </section>

  <section class="specialties">
    <h2>HVAC Specialits</h2>
    <p>Lorem ipsum dolor sit amet consectetur. Hac in volutpat luctus in eu. Nisi diam purus quam tortor. Enim natoque metus lacus nunc ac congue. Id tempus pellentesque blandit nunc lectus orci lorem. At massa faucibus ac vel pulvinar interdum donec est. Ultrices congue rhoncus congue eget sem.</p>
    <div class="gallery">
      <div class="shot" role="img" aria-label="Technicians working on an outdoor unit" style="background:linear-gradient(135deg,#8b8f95,#d0892a)"></div>
      <div class="shot" role="img" aria-label="Worker on a ladder installing ducting" style="background:linear-gradient(135deg,#c9c6bf,#8a8f99)"></div>
      <div class="shot" role="img" aria-label="Technician servicing a ceiling unit" style="background:linear-gradient(135deg,#dfe6ee,#2f5fb5)"></div>
      <div class="shot" role="img" aria-label="Rows of rooftop condenser units" style="background:linear-gradient(135deg,#b7bcc3,#6d747e)"></div>
      <div class="shot" role="img" aria-label="Condenser units against a blue sky" style="background:linear-gradient(135deg,#3c6fc2,#a8b3c2)"></div>
      <span class="arrow" style="left:162px"><svg width="10" height="10" viewBox="0 0 10 10"><path d="M7 1L3 5l4 4" fill="none" stroke="#333" stroke-width="1.6"/></svg></span>
      <span class="arrow" style="right:92px"><svg width="10" height="10" viewBox="0 0 10 10"><path d="M3 1l4 4-4 4" fill="none" stroke="#333" stroke-width="1.6"/></svg></span>
    </div>
    <span class="btn">Schedule an appointment</span>
  </section>

  <section class="feedback" role="region" aria-label="Customer feedback">
    <h2>Read Our Latest Customer Feedback</h2>
    <div class="reviews">
      <div class="review">
        <div class="stars"><svg width="100" height="18" viewBox="0 0 100 18" fill="var(--blue)"><g id="s"><path d="M9 0l2.6 5.8 6.4.6-4.8 4.3 1.4 6.3L9 13.8 3.4 17l1.4-6.3L0 6.4l6.4-.6z"/></g><use href="#s" x="20"/><use href="#s" x="40"/><use href="#s" x="60"/><use href="#s" x="80"/></svg></div>
        <p>Lorem ipsum dolor sit amet consectetur. Hac in volutpat luctus in eu. Nisi diam purus quam tortor.</p>
        <div class="reviewer"><span class="av"></span><div><b>Dorvan</b><span>2 March 2024</span></div></div>
      </div>
      <div class="review">
        <div class="stars"><svg width="100" height="18" viewBox="0 0 100 18" fill="var(--blue)"><use href="#s"/><use href="#s" x="20"/><use href="#s" x="40"/><use href="#s" x="60"/><use href="#s" x="80"/></svg></div>
        <p>Lorem ipsum dolor sit amet consectetur. Hac in volutpat luctus in eu. Nisi diam purus quam tortor.</p>
        <div class="reviewer"><span class="av"></span><div><b>Dorvan</b><span>2 March 2024</span></div></div>
      </div>
      <div class="review">
        <div class="stars"><svg width="100" height="18" viewBox="0 0 100 18" fill="var(--blue)"><use href="#s"/><use href="#s" x="20"/><use href="#s" x="40"/><use href="#s" x="60"/><use href="#s" x="80"/></svg></div>
        <p>Lorem ipsum dolor sit amet consectetur. Hac in volutpat luctus in eu. Nisi diam purus quam tortor.</p>
        <div class="reviewer"><span class="av"></span><div><b>Dorvan</b><span>2 March 2024</span></div></div>
      </div>
      <div class="review">
        <div class="stars"><svg width="100" height="18" viewBox="0 0 100 18" fill="var(--blue)"><use href="#s"/><use href="#s" x="20"/><use href="#s" x="40"/><use href="#s" x="60"/><use href="#s" x="80"/></svg></div>
        <p>Lorem ipsum dolor sit amet consectetur. Hac in volutpat luctus in eu. Nisi diam purus quam tortor.</p>
        <div class="reviewer"><span class="av"></span><div><b>Dorvan</b><span>2 March 2024</span></div></div>
      </div>
    </div>
  </section>

  <section class="cta">
    <h2>Call today to find out how our<br>HVAC installation, maintenance &amp;<br>repair services can save you money!</h2>
    <div class="cta-row">
      <span class="btn">Schedule an appointment</span>
      <span class="phone"><svg width="18" height="18" viewBox="0 0 24 24" fill="none" stroke="var(--sky)" stroke-width="2"><path d="M22 16.9v3a2 2 0 0 1-2.2 2 19.8 19.8 0 0 1-8.6-3.1 19.5 19.5 0 0 1-6-6A19.8 19.8 0 0 1 2.1 4.2 2 2 0 0 1 4.1 2h3a2 2 0 0 1 2 1.7c.1.9.4 1.8.7 2.7a2 2 0 0 1-.5 2.1L8 9.8a16 16 0 0 0 6 6l1.3-1.3a2 2 0 0 1 2.1-.4c.9.3 1.8.6 2.7.7a2 2 0 0 1 1.7 2z"/></svg>555-014-2780</span>
    </div>
  </section>

  <section class="contact">
    <ul class="contact-info">
      <li><span class="ci"><svg width="10" height="10" viewBox="0 0 24 24" fill="#fff"><path d="M22 16.9v3a2 2 0 0 1-2.2 2A19.8 19.8 0 0 1 2.1 4.2 2 2 0 0 1 4.1 2h3l2 5-2.5 2a16 16 0 0 0 7.4 7.4l2-2.5z"/></svg></span>555-014-2780</li>
      <li><span class="ci"><svg width="10" height="10" viewBox="0 0 24 24" fill="none" stroke="#fff" stroke-width="3"><rect x="2" y="5" width="20" height="14"/><path d="M2 5l10 8 10-8"/></svg></span>info@tidewellhvac.example</li>
      <li><span class="ci"><svg width="10" height="10" viewBox="0 0 24 24" fill="#fff"><path d="M12 1a8 8 0 0 0-8 8c0 6 8 14 8 14s8-8 8-14a8 8 0 0 0-8-8zm0 11a3 3 0 1 1 0-6 3 3 0 0 1 0 6z"/></svg></span>4820 Harbor Lane Suite 210,<br>Baymont, FL 33099</li>
    </ul>
    <div class="map" role="img" aria-label="Street map showing the office location"></div>
    <div class="form">
      <h2>Request a Call Back<br>Today Now!</h2>
      <div class="fields">
        <div class="field">First name</div>
        <div class="field">Last name</div>
        <div class="field">Email</div>
        <div class="field">Phone Number</div>
        <div class="field wide">Message</div>
      </div>
      <span class="btn">Send</span>
    </div>
  </section>

  <footer class="footer">
    <div class="brand"><span class="dot"></span>Tidewell HVAC</div>
    <div class="fcol" style="left:462px">
      <h4>CONTACT</h4>
      <ul>
        <li class="ic"><i></i>555-014-2780</li>
        <li class="ic"><i></i>info@tidewellhvac.example</li>
        <li class="ic"><i></i>4820 Harbor Lane Suite 210,<br>Baymont, FL 33099</li>
      </ul>
    </div>
    <div class="fcol" style="left:683px">
      <h4>QUICKLINKS</h4>
      <ul><li>Home</li><li>About Us</li><li>Contact Us</li></ul>
    </div>
    <div class="fcol" style="left:848px">
      <h4>OUR SERVICES</h4>
      <ul><li>Gas Fitting/Piping</li><li>Service &amp; Instllation</li><li>Residential &amp; Commercials</li><li>Building Automation &amp; Controls</li></ul>
    </div>
  </footer>
  <div class="copy">
    <span>All Content Copyright ©2024 Tidewell HVAC</span>
    <span class="socials" aria-label="Social links"><span></span><span></span><span></span><span></span></span>
  </div>

</div>
</body>
</html>
```